Stretch on the Green with Mira

I want to advertise my Stretch on the Green classes for Summer. Classes are outside at the lovely local park. Holloway field. 83 Marangi St. Sandringham.
Classes are for beginners to advance levels.
Classes start Monday, October 17th.
Monday 6pm Beginners
Tuesday 6pm Intermediate
Thursday 6pm Intermediate/Advance
Saturday 9am All fitness levels
My Pilates classes are specially designed to help improve strength and flexibility but as well will also improve posture, reduce stress and develop control and endurance in the entire body.
Booking essential. Limited numbers so I can make sure the correct technique is always being followed.
For more info or to book contact details:
Mira 027358164
mira@corewithmira.net
www.corewithmira.net
$15 Per Session

Target Market(s)

Males and Females ages 35plus.

Industry/Entity Type

Fitness

Font styles to use
Sans Serif

Requirements
Must have
• My logo. Contact details. A Park that looks lovely to exercise at.
Nice to have
• Summer looking. Trees - inspiration to be exercising outside

```html
<!DOCTYPE html>
<html lang="en">
<head>
<meta charset="utf-8">
<title>Stretch on the Green with Mira</title>
<link rel="stylesheet" href="https://fonts.googleapis.com/css2?family=Montserrat:wght@500;600;700;800&family=Oswald:wght@500;600&display=swap">
<style>
:root{
  --backdrop:#2b2b2b;
  --pink:#e4097f;
  --pink-band:rgba(200,30,100,.78);
  --teal:#2cc9a0;
  --lime:#b5f21f;
  --ink:#1d1d1d;
  --white:#ffffff;
  --slate:#5a5a5c;
}
*{margin:0;padding:0;box-sizing:border-box}
html,body{width:1200px;height:1177px;overflow:hidden;background:var(--backdrop)}
body{font-family:"Montserrat",sans-serif;position:relative}
.flyer{position:absolute;left:253px;top:109px;width:750px;height:970px;background:var(--white);overflow:hidden}
.park-photo{position:absolute;left:0;top:0;width:750px;height:600px;
  background:radial-gradient(ellipse at 75% 30%,#7fa860 0%,rgba(127,168,96,0) 45%),
  linear-gradient(180deg,#9fb98a 0%,#6f9a55 40%,#5c8a3e 70%,#7aa548 100%)}
.title-band{position:absolute;left:0;top:41px;width:548px;height:114px;background:var(--pink-band);display:flex;align-items:center}
.title-main{margin-left:46px;font-weight:800;font-size:96px;line-height:1;color:var(--white);white-space:nowrap}
.title-sub{position:absolute;right:24px;top:172px;text-align:left;color:var(--white);font-weight:600;line-height:.9;white-space:nowrap}
.title-sub .small{display:block;font-size:46px}
.title-sub .big{display:block;font-size:96px;font-weight:700}
.dots{position:absolute;left:514px;top:307px}
.info-box{position:absolute;top:475px;height:121px;width:190px;text-align:center;border-radius:6px;box-shadow:0 3px 6px rgba(0,0,0,.25);white-space:nowrap}
.info-levels{left:55px;background:var(--pink);color:var(--white);font-size:16px;font-weight:600;padding-top:58px;line-height:1.25}
.info-start{left:289px;width:192px;background:var(--white);color:var(--teal);font-size:16px;font-weight:700;padding-top:12px;line-height:1.1}
.info-start .day{color:var(--pink);display:block}
.info-start .date{font-family:"Oswald",sans-serif;color:var(--pink);font-size:58px;font-weight:600;line-height:1;display:block;margin-top:4px}
.info-start .date sup{font-size:28px;vertical-align:14px}
.info-place{left:527px;background:var(--teal);color:var(--white);font-size:16px;font-weight:700;padding-top:56px;line-height:1.25}
.box-icon{position:absolute;left:50%;top:10px;transform:translateX(-50%)}
.curve{position:absolute;left:0;top:520px}
.intro{position:absolute;left:0;width:750px;top:617px;text-align:center;font-size:15.5px;font-weight:600;color:var(--ink);line-height:1.3;white-space:nowrap}
.schedule{position:absolute;left:181px;top:725px;list-style:none;font-size:15px;font-weight:600;color:var(--ink)}
.schedule li{height:20.5px;display:flex;align-items:center;white-space:nowrap}
.schedule li > *{flex-shrink:0}
.schedule .arrow{width:0;height:0;border-top:5px solid transparent;border-bottom:5px solid transparent;border-left:6px solid var(--pink);margin-right:7px}
.schedule .day{width:78px;color:var(--pink);font-weight:700}
.schedule .teal .day{color:var(--teal)}
.schedule .teal .arrow{border-left-color:var(--teal)}
.schedule .time{width:55px}
.schedule .long .time{width:57px}
.price{position:absolute;left:560px;top:669px;width:136px;height:136px;border-radius:50%;background:var(--white);border:3px solid var(--teal)}
.price-inner{position:absolute;left:8px;top:8px;width:114px;height:114px;border-radius:50%;background:var(--pink);color:var(--white);text-align:center;font-weight:700;font-size:15px;line-height:1.05}
.price-inner .amount{display:block;font-size:44px;font-weight:800;margin-top:14px;line-height:1}
.price-inner .amount span{color:var(--lime)}
.booking{position:absolute;left:0;top:824px;width:750px;height:34px;background:var(--pink);display:flex;align-items:center;color:var(--white);font-weight:600;font-size:11.5px;white-space:nowrap}
.booking-label{flex-shrink:0;width:181px;height:34px;background:var(--teal);display:flex;align-items:center;justify-content:center;font-weight:700;font-size:12.5px}
.booking-note{padding-left:10px}
.accent-line{position:absolute;left:0;top:858px;width:750px;height:7px;background:var(--lime)}
.footer-panel{position:absolute;left:0;top:865px}
.brand{position:absolute;left:0;top:925px;width:330px;height:30px;display:flex;align-items:center;justify-content:center;gap:10px;color:var(--pink);font-size:19px;font-weight:600;letter-spacing:1px;white-space:nowrap}
.brand-mark{width:11px;height:11px;border-radius:50%;background:var(--pink)}
.contact{position:absolute;left:358px;top:882px;font-size:13px;font-weight:600;color:var(--ink);line-height:18px;white-space:nowrap}
.contact h2{font-size:13.5px;font-weight:700;margin-left:20px;line-height:18px}
.contact p{display:flex;align-items:center;gap:6px;height:18px}
.contact p.web-line{height:24px}
.contact .name{color:var(--pink)}
.contact .web{color:var(--pink);font-size:17px;font-weight:800}
</style>
</head>
<body>
<main class="flyer">
  <div class="park-photo" role="img" aria-label="Photo of a woman doing a plank on an exercise ball on the grass of a sunny tree-lined park"></div>

  <div class="title-band"><h1 class="title-main">STRETCH</h1></div>
  <p class="title-sub"><span class="small">on the</span><span class="big">green</span></p>
  <svg class="dots" width="212" height="12" viewBox="0 0 212 12">
    <line x1="5" y1="6" x2="207" y2="6" stroke="#b5f21f" stroke-width="7" stroke-linecap="round" stroke-dasharray="0 11.2"/>
  </svg>

  <svg class="curve" width="750" height="200" viewBox="0 0 750 200">
    <path d="M0 40 Q375 -10 750 40 L750 160 Q375 215 0 160 Z" fill="#b5f21f"/>
  </svg>

  <div class="info-box info-levels">
    <svg class="box-icon" width="44" height="44" viewBox="0 0 44 44"><circle cx="20" cy="24" r="17" fill="none" stroke="#fff" stroke-width="3.5"/><path d="M11 23 L20 31 L40 6" fill="none" stroke="#fff" stroke-width="4" stroke-linecap="round" stroke-linejoin="round"/></svg>
    Classes are for<br>BEGINNERS to<br>ADVANCE levels
  </div>
  <div class="info-box info-start">
    Classes start<span class="day">MONDAY</span><span class="date">17<sup>TH</sup>OCT</span>
  </div>
  <div class="info-box info-place">
    <svg class="box-icon" width="28" height="38" viewBox="0 0 28 38"><path d="M14 2 C6 2 2 8 2 14 C2 23 14 36 14 36 C14 36 26 23 26 14 C26 8 22 2 14 2 Z" fill="#fff"/><circle cx="14" cy="14" r="5" fill="#2cc9a0"/></svg>
    HOLLOWAY FIELD<br>83 Marangi St.<br>Sandringham.
  </div>

  <p class="intro">My Pilates classes are specially designed to help improve strength and flexibility<br>but as well will also improve posture, reduce stress and develop control<br>and endurance in the entire body.</p>

  <ul class="schedule">
    <li><i class="arrow"></i><span class="day">Monday</span><span class="time">6pm</span><span>Beginners</span></li>
    <li class="teal"><i class="arrow"></i><span class="day">Tuesday</span><span class="time">6pm</span><span>Intermediate</span></li>
    <li class="long"><i class="arrow"></i><span class="day">Thursday</span><span class="time">6pm</span><span>Intermediate/Advance</span></li>
    <li class="teal long"><i class="arrow"></i><span class="day">Saturday</span><span class="time">9am</span><span>All fitness levels</span></li>
  </ul>

  <div class="price"><div class="price-inner"><span class="amount">15<span>$</span></span>per<br>session</div></div>

  <div class="booking"><span class="booking-label">BOOKING ESSENTIAL</span><span class="booking-note">Limited numbers so I can make sure the correct technique is always being followed.</span></div>
  <div class="accent-line"></div>

  <svg class="footer-panel" width="750" height="105" viewBox="0 0 750 105"><path d="M0 0 H290 L343 105 H0 Z" fill="#5a5a5c"/></svg>
  <div class="brand"><i class="brand-mark"></i>CORE WITH MIRA</div>

  <div class="contact">
    <h2>FOR MORE INFO OR TO BOOK CONTACT DETAILS:</h2>
    <p><svg width="13" height="13" viewBox="0 0 24 24"><path d="M6 2 L10 7 L8 10 C9 13 11 15 14 16 L17 14 L22 18 L19 22 C10 21 3 14 2 5 Z" fill="#e4097f"/></svg><span class="name">Mira</span> 027358164</p>
    <p><svg width="13" height="10" viewBox="0 0 24 18"><rect x="0" y="0" width="24" height="18" fill="#e4097f"/><path d="M0 0 L12 10 L24 0" fill="none" stroke="#fff" stroke-width="2"/></svg>mira@corewithmira.net</p>
    <p class="web-line"><svg width="14" height="14" viewBox="0 0 24 24"><circle cx="12" cy="12" r="10" fill="none" stroke="#e4097f" stroke-width="2.5"/><path d="M2 12 H22 M12 2 C7 7 7 17 12 22 M12 2 C17 7 17 17 12 22" fill="none" stroke="#e4097f" stroke-width="2"/></svg><span class="web">www.corewithmira.net</span></p>
  </div>
</main>
</body>
</html>
```